New look while maintaining the Brand identification!

I want a new look for my business card. I want to keep the same colors and feel but change the look and layout a bit. The logo (KALMORETIX Physical therapy Reimagined and the lilypad) must remain the same and in that font.
We are a physical therapy clinic. So we have certification that we can write on the back or services we provide (which is what we currently have on the back of the card as well)

Contact information
2840 Cedar Hollow Rd., #22
Naples, FL 34276
P: (239) 555-0172
F: (239) 555-0198
E: kalmoretixcare@mailvexo.com
W: www.kalmoretixcare-example.com

Industry/Entity Type

Physical Therapy

Contact Information for Business Card

Our current cards have the business address and information on the back. But I am willing to have it be in the front.

Font styles to use
Sans Serif

Colors
abd036
fbf289
ec1f27

Requirements
Must have
• Has to be unique!
• Services we provide and/or techniques we do must fit on the card
Nice to have
• Would like to have the front and back somehow linked together. Such that if you set the front next to the back, there is a nice flow of design! Currently the back is white with writing on it.
Should not have
• I like the wave lines as compared to straight lines.

```html
<!DOCTYPE html>
<html lang="en">
<head>
<meta charset="utf-8">
<title>Kalmoretix Business Card</title>
<link href="https://fonts.googleapis.com/css2?family=Open+Sans:wght@400;600;700&family=Ubuntu:wght@500&display=swap" rel="stylesheet">
<style>
  :root {
    --backdrop: #3a3230;
    --card: #ffffff;
    --gold: #d6b600;
    --olive: #5f7418;
    --rust: #c2612a;
    --ink: #3a3a3a;
    --ink-soft: #505050;
  }
  html, body {
    margin: 0;
    width: 1200px;
    height: 844px;
    overflow: hidden;
    background: var(--backdrop);
    font-family: "Open Sans", Arial, sans-serif;
  }
  .stage {
    position: relative;
    width: 1200px;
    height: 844px;
  }
  .card {
    position: absolute;
    top: 272px;
    width: 520px;
    height: 300px;
    background: var(--card);
    box-shadow: 0 10px 24px rgba(0,0,0,.45);
    overflow: hidden;
  }
  .card--contact { left: 50px; }
  .card--appointment { left: 630px; }

  /* contact side */
  .band-top {
    position: absolute; left: 0; right: 0; top: 0;
    height: 10px; background: var(--gold);
  }
  .band-bottom {
    position: absolute; left: 0; right: 0; bottom: 0;
    height: 16px; background: var(--gold);
  }
  .contact-body {
    position: absolute; left: 0; right: 0; top: 26px;
    text-align: center;
  }
  .tagline {
    font-family: "Ubuntu", "Open Sans", sans-serif;
    font-weight: 500;
    font-size: 21px;
    margin: 0 0 10px 60px;
  }
  .tagline__lead { color: var(--olive); }
  .tagline__accent { color: var(--rust); }
  .person {
    margin: 0 0 18px -30px;
    font-size: 21px;
    font-weight: 700;
    color: var(--ink);
  }
  .person__role {
    font-size: 13px;
    font-weight: 400;
    color: var(--ink-soft);
  }
  .person__divider { font-weight: 400; margin: 0 4px; }
  .details {
    list-style: none; margin: 0; padding: 0;
    font-size: 14px; line-height: 21px; color: var(--ink);
  }
  .details__address { margin-top: 12px; }
  .services {
    margin: 16px 0 0;
    font-size: 14.5px; font-weight: 700; line-height: 22px;
    color: var(--gold);
  }
  .services .sep { font-weight: 400; margin: 0 5px; }

  /* appointment side */
  .tab-right {
    position: absolute; right: 0; top: 56px;
    width: 36px; height: 52px; background: var(--gold);
  }
  .tab-left {
    position: absolute; left: 0; top: 168px;
    width: 34px; height: 54px; background: var(--gold);
  }
  .brand {
    position: absolute; left: 100px; top: 62px;
    display: flex; align-items: center; gap: 12px;
  }
  .brand__mark {
    width: 22px; height: 22px; border-radius: 50%;
    background: var(--olive);
  }
  .brand__name {
    font-size: 46px; font-weight: 700; letter-spacing: 1px;
    color: var(--gold);
  }
  .appointment {
    position: absolute; left: 84px; top: 172px;
    width: 380px;
  }
  .appointment__label {
    font-size: 16px; color: var(--rust); margin: 0 0 6px;
  }
  .appointment__line {
    height: 2px; background: var(--gold); margin: 0 0 0 36px;
  }
  .appointment__line + .appointment__line { margin-top: 34px; margin-left: 36px; }
  .appointment__line:first-of-type { margin-left: 140px; margin-top: -14px; }
</style>
</head>
<body>
<main class="stage">
  <section class="card card--contact" aria-label="Contact side">
    <div class="band-top"></div>
    <div class="contact-body">
      <p class="tagline"><span class="tagline__lead">Physical Therapy</span> <span class="tagline__accent">Reimagined</span></p>
      <p class="person">Daniel Harlow<span class="person__divider">|</span><span class="person__role">Managing Director</span></p>
      <ul class="details">
        <li>(044)-555-0126</li>
        <li>info@kalmoretixmail.com</li>
        <li>www.kalmoretixcare-example.com</li>
        <li class="details__address">2840 Cedar Hollow Rd., #22 Naples, FL 34276</li>
      </ul>
      <p class="services">
        Neck Pain<span class="sep">|</span>Back Pain<span class="sep">|</span>Hip Pain<span class="sep">|</span>Shoulder Pain<br>
        Vertigo<span class="sep">|</span>Fibromyalgia<span class="sep">|</span>Plantar Fasciitis<span class="sep">|</span>Migraine
      </p>
    </div>
    <div class="band-bottom"></div>
  </section>

  <section class="card card--appointment" aria-label="Appointment side">
    <div class="tab-right"></div>
    <div class="tab-left"></div>
    <div class="brand">
      <span class="brand__mark"></span>
      <span class="brand__name">KALMORETIX</span>
    </div>
    <div class="appointment">
      <p class="appointment__label">Appointment</p>
      <div class="appointment__line"></div>
      <div class="appointment__line"></div>
    </div>
  </section>
</main>
</body>
</html>
```